Hörbuchcover
Zielgruppe
Spiritueller Hörbuchverlag für ganzheitliche Gesundheit, Glück und Wohlstand.
Aufgabenstellung
Benötigt wird ein schönes quadratisches Cover, 2400x2400 mindestens 72dpi für ein Hörbuchcover.
Auf dem Cover soll eine gelb/orange Rose zu in Form einer Blüte zu sehen sein.
Titel: Innere Wandlung
Untertitel: Emotionen sind der Schlüssel für Gesundheit, Energie & Lebensfreude
Autorenname: Dr. med. Birgit Wolkenstein
Das Feloria Logo soll unten mittig sitzen.
Es folgen weiterer Hörbücher von dieser Autorin und es wäre gut wenn man die folgenden Cover in einem ähnlichen Stil halten könnte. Ein harmonisches und gut zu erkennendes Design mit hohem Wiedererkennungseffekt. Ich freue mich auf kreative Designvorschläge.
Auf feloria.de kann man sehen wo das Logo sitzen soll.
Herzliche Grüße - Jens

```html
<!DOCTYPE html>
<html lang="de">
<head>
<meta charset="utf-8">
<title>Innere Wandlung – Hörbuchcover</title>
<link rel="stylesheet" href="https://fonts.googleapis.com/css2?family=Amatic+SC:wght@700&family=Montserrat:wght@500;600&display=swap">
<style>
  :root {
    --stage: #7a7a7a;
    --maroon: #6a1c20;
    --orange: #ec5f24;
    --petal-light: #fff6dc;
    --petal-mid: #fcd874;
    --petal-deep: #f4a42e;
    --glow: rgba(255, 255, 255, 0.95);
  }
  * { margin: 0; padding: 0; box-sizing: border-box; }
  html, body {
    width: 807px;
    height: 1200px;
    overflow: hidden;
    background: var(--stage);
  }
  .cover {
    position: absolute;
    left: 43px;
    top: 240px;
    width: 720px;
    height: 720px;
    overflow: hidden;
    box-shadow: 0 4px 10px rgba(0, 0, 0, 0.35);
  }
  .cover__rose {
    position: absolute;
    inset: 0;
    background:
      radial-gradient(ellipse 42% 46% at 44% 46%, var(--glow) 0%, rgba(255,255,255,0.6) 45%, rgba(255,255,255,0) 100%),
      radial-gradient(circle at 88% 42%, #fff1c4 0%, var(--petal-mid) 22%, var(--petal-deep) 55%, rgba(244,164,46,0) 80%),
      radial-gradient(circle at 10% 8%, #ffd84a 0%, rgba(255,216,74,0) 40%),
      radial-gradient(circle at 95% 95%, #f39a2c 0%, rgba(243,154,44,0) 40%),
      linear-gradient(160deg, #fde48a 0%, var(--petal-light) 45%, #fbd47a 75%, #f5a93a 100%);
  }
  .cover__author {
    position: absolute;
    top: 88px;
    left: 0;
    width: 100%;
    text-align: center;
    font-family: "Montserrat", sans-serif;
    font-weight: 600;
    font-size: 20px;
    letter-spacing: 0.2em;
    color: var(--maroon);
    text-transform: uppercase;
  }
  .cover__title {
    position: absolute;
    top: 140px;
    left: 0;
    width: 100%;
    text-align: center;
    font-family: "Amatic SC", sans-serif;
    font-weight: 700;
    font-size: 182px;
    line-height: 138px;
    color: var(--maroon);
    text-transform: uppercase;
    text-shadow: 0 0 18px var(--glow), 0 0 34px var(--glow);
  }
  .cover__title span { display: block; }
  .cover__subtitle {
    position: absolute;
    top: 462px;
    left: 0;
    width: 100%;
    text-align: center;
    font-family: "Montserrat", sans-serif;
    font-weight: 600;
    font-size: 21px;
    line-height: 30px;
    color: var(--orange);
  }
  .publisher {
    position: absolute;
    top: 612px;
    left: 0;
    width: 100%;
    display: flex;
    justify-content: center;
    align-items: center;
    gap: 12px;
  }
  .publisher__dot {
    width: 22px;
    height: 22px;
    border-radius: 50%;
    background: var(--maroon);
  }
  .publisher__name {
    font-family: "Montserrat", sans-serif;
    font-weight: 500;
    font-size: 32px;
    letter-spacing: 0.12em;
    color: var(--maroon);
    text-transform: uppercase;
  }
</style>
</head>
<body>
  <main class="cover">
    <div class="cover__rose" role="img" aria-label="Nahaufnahme einer gelb-orangen Rosenblüte mit weichem, hellem Lichtschein"></div>
    <p class="cover__author">Dr. med. Birgit Wolkenstein</p>
    <h1 class="cover__title"><span>Innere</span><span>Wandlung</span></h1>
    <p class="cover__subtitle">Emotionen sind der Schlüssel für<br>Gesundheit, Energie &amp; Lebensfreude</p>
    <div class="publisher">
      <span class="publisher__dot"></span>
      <span class="publisher__name">Feloria</span>
    </div>
  </main>
</body>
</html>
```